zVerda Corporate Website

zVerda is a well-funded start up developing an Online Marketing Platform for small businesses in Europe.
We are launching in February 2012 with all-in-one online marketing services including professional website, DIY SEO, Dashboard with Reports and Online marketing tools, and Support.
Our internal web designer has come up with a preliminary website design which we wish to continue to improve using new ideas, colours, layout, image, etc.
The brief is very simple - improve the website whether it is look & feel, ease of use, conversion rate - we are looking for overall improvements.
The contest will last 5 days and we will award the winner £300.
If you are the winner , you will also be required to provide designs for 3 more internal pages adhering to the proposed home page design.
Judging criteria : -
Visual Design
Layout must adhere to best practices and wire frame. If you decide to move elements around significantly please provide reason
Functional, informative and drives calls to action
Industry/Entity Type
Marketing
Look and feel
Each slider illustrates characteristics of the customer's brand and the style your logo design should communicate.

```html
<!DOCTYPE html>
<html lang="en">
<head>
<meta charset="utf-8">
<title>zVerda – Online Marketing for Small Business</title>
<link href="https://fonts.googleapis.com/css2?family=Arimo:wght@400;700&family=Tinos:ital@1&display=swap" rel="stylesheet">
<style>
:root{
  --blue:#16a5e0;--blue-dark:#0a86c4;--blue-text:#2a8fc8;
  --ink:#333;--grey:#9a9a9a;--light:#f7f8f9;--orange:#f7941d;
  --footer:#262626;--footer-2:#1b1b1b;--navy:#1f3e95;
}
*{box-sizing:border-box;margin:0;padding:0}
html,body{width:874px;height:1200px;overflow:hidden}
body{font-family:"Arimo",Arial,sans-serif;background:var(--light);position:relative;color:var(--ink)}
.abs{position:absolute}
/* header */
.header{left:0;top:0;width:874px;height:90px;background:linear-gradient(#3ac0f0,#12a0dc)}
.header::before{content:"";position:absolute;left:0;top:0;width:100%;height:18px;background:#0d97d4}
.toplinks{right:82px;top:4px;font-size:9px;color:#fff}
.toplinks span{margin:0 6px}
.brand{left:72px;top:42px;display:flex;align-items:center;gap:8px;color:#fff;font-size:30px;font-weight:700}
.brand i{width:28px;height:28px;border-radius:50%;background:var(--navy);display:block}
.nav{top:47px;font-size:16px;color:#fff}
.nav.home{left:557px;width:81px;height:27px;background:#fff;color:var(--blue-dark);border-radius:3px;text-align:center;line-height:27px}
/* hero */
.hero{left:0;top:90px;width:874px;height:275px;background:linear-gradient(#fff,#f2f4f5)}
.ticks{left:78px;top:118px;list-style:none;font-size:14px;color:#666}
.ticks li{height:24px;display:flex;align-items:center;gap:10px}
.ticks svg{width:14px;height:12px}
.tagline{left:61px;top:222px;color:var(--orange);font-size:19px;line-height:23px}
.signup{left:72px;top:297px;width:238px;height:35px;background:linear-gradient(#4a4a4a,#1e1e1e);border-radius:3px;color:var(--blue);font-size:14px;display:flex;align-items:center;padding-left:12px;box-shadow:0 3px 4px rgba(0,0,0,.3)}
.signup b{position:absolute;right:8px;top:6px;width:23px;height:23px;border-radius:50%;background:#fff}
.signup b::after{content:"";position:absolute;left:9px;top:6px;border-left:7px solid var(--blue-dark);border-top:5px solid transparent;border-bottom:5px solid transparent}
.person{left:486px;top:130px;width:232px;height:235px;background:radial-gradient(circle at 50% 40%,#d9a88a,#7a4a2e 55%,#3b2519 85%,#f2f4f5 86%)}
.bubble{position:absolute;width:107px;height:28px;background:linear-gradient(#eaf8fe,#c9ecfb);color:var(--blue-text);font-size:12px;line-height:28px;text-align:center;white-space:nowrap;box-shadow:0 1px 2px rgba(0,0,0,.12)}
.bubble::after{content:"";position:absolute;right:14px;bottom:-7px;border-top:7px solid #c9ecfb;border-left:9px solid transparent}
/* band */
.band{left:0;top:365px;width:874px;height:71px;background:linear-gradient(#f5f5f5,#dcdcdc);text-align:center}
.band h1{font-size:21px;color:#222;margin-top:12px}
.band p{font-size:16px;color:var(--blue-text);margin-top:6px}
.how{left:0;top:453px;width:874px;text-align:center;font-size:33px;color:#b5b5b5;font-weight:400}
/* offer tiles */
.tile{top:514px;width:221px;height:191px;overflow:hidden;box-shadow:0 4px 6px rgba(0,0,0,.25)}
.tile.setup{left:76px;background:radial-gradient(circle at 60% 55%,#f7a21a,#e2401a 70%)}
.tile.pro{left:327px;background:radial-gradient(circle at 60% 55%,#8ee22b,#1a9e1a 70%)}
.tile.turbo{left:578px;background:radial-gradient(circle at 60% 55%,#3fc6f7,#0a6dc4 70%)}
.tile .corner{position:absolute;right:0;top:0;width:0;height:0;border-top:72px solid #1ba3e4;border-left:72px solid transparent}
.tile.setup .corner{border-top:95px solid #f2c02a;border-left:95px solid transparent}
.price{position:absolute;right:6px;top:6px;color:#fff;font-size:30px;font-weight:700;text-align:right;line-height:30px}
.price small{display:block;font-size:12px;line-height:14px}
.burst{position:absolute;left:12px;top:46px;width:94px;height:94px}
.burst span{position:absolute;inset:0;display:flex;align-items:center;justify-content:center;text-align:center;font-weight:700;color:#444;font-size:12px;line-height:13px;transform:rotate(-20deg)}
.tile .lead{position:absolute;right:10px;top:100px;color:#fff;text-align:right;font-size:12px;line-height:14px;font-weight:700}
.tile .lead em{display:block;font-style:normal;font-size:18px;line-height:22px;font-weight:400}
.tile .foot{position:absolute;left:0;bottom:0;width:100%;height:47px;color:#fff;text-align:center;font-size:15px;line-height:17px;display:flex;align-items:center;justify-content:center}
.setup .foot{background:#5c2a20;font-size:17px}
.pro .foot{background:#2b5e1c}
.turbo .foot{background:#1c4564}
.divider{left:40px;top:724px;width:786px;height:2px;background:#ddd}
/* slider */
.slider{left:63px;top:753px;width:747px;height:96px;background:linear-gradient(#fff,#e6e8ea);border-radius:6px;box-shadow:0 2px 4px rgba(0,0,0,.2)}
.thumb{top:766px;width:156px;height:72px;background:linear-gradient(#7a2030 0 18%,#e9e4d6 18%)}
.arrow{top:793px;width:16px;height:16px;border-radius:50%;background:#7cc61e}
.arrow::after{content:"";position:absolute;top:4px;border-top:4px solid transparent;border-bottom:4px solid transparent}
.arrow.prev{left:69px}.arrow.prev::after{left:5px;border-right:5px solid #fff}
.arrow.next{left:784px}.arrow.next::after{left:6px;border-left:5px solid #fff}
/* testimonial */
.author{left:100px;top:889px;width:100px;text-align:center;color:var(--blue-text);font-size:14px}
.author small{display:block;color:var(--grey);font-size:10px;margin-top:2px}
.quote{left:212px;top:871px;width:537px;height:68px;background:#fff;border:1px solid #e5e5e5;border-radius:4px;padding:13px 20px 0 56px;font-family:"Tinos",serif;font-style:italic;font-size:12px;line-height:18px;color:#999}
.quote::before{content:"\201C";position:absolute;left:14px;top:6px;font-size:54px;line-height:54px;color:#ddd;font-family:"Tinos",serif}
/* cards */
.card{top:968px;width:182px;height:77px;background:#fff;border:1px solid #e3e3e3;border-radius:3px}
.card h3{height:20px;background:linear-gradient(#fff,#ececec);font-size:12px;font-weight:400;color:#666;text-align:center;line-height:20px;letter-spacing:.5px}
.card .ico{position:absolute;left:8px;top:30px;width:36px;height:36px;border-radius:4px}
.card p{position:absolute;left:64px;top:30px;width:108px;font-size:10px;line-height:13px;color:#bbb}
/* footer */
.footer{left:0;top:1071px;width:874px;height:96px;background:var(--footer)}
.fcol{top:1085px;font-size:10px;line-height:19px;color:#eee}
.fcol li{list-style:none}
.news h4{font-size:12px;font-weight:400;color:#eee}
.news .field{position:absolute;top:26px;left:0;width:162px;height:23px;background:#4a4a4a;font-size:10px;color:#ccc;line-height:23px;padding-left:8px}
.news .go{position:absolute;top:26px;left:162px;width:33px;height:23px;background:var(--blue);color:#fff;font-size:11px;font-weight:700;text-align:center;line-height:23px}
.copy{left:0;top:1167px;width:874px;height:33px;background:var(--footer-2);color:#888;font-size:10px;text-align:center;line-height:33px}
</style>
</head>
<body>
<svg width="0" height="0" style="position:absolute">
  <defs>
    <polygon id="star" points="98,50 88.6,60.4 91.6,74 78.3,78.3 74,91.6 60.4,88.6 50,98 39.6,88.6 26,91.6 21.7,78.3 8.4,74 11.4,60.4 2,50 11.4,39.6 8.4,26 21.7,21.7 26,8.4 39.6,11.4 50,2 60.4,11.4 74,8.4 78.3,21.7 91.6,26 88.6,39.6"/>
    <path id="tick" d="M1 6 L5 10 L13 1" fill="none" stroke="#1aa3e0" stroke-width="3"/>
  </defs>
</svg>

<header class="abs header"></header>
<div class="abs toplinks">About Us<span>|</span>Contact Us<span>|</span>login</div>
<div class="abs brand"><i></i>zVerda</div>
<div class="abs nav home">Home</div>
<div class="abs nav" style="left:659px">Quick Tour</div>
<div class="abs nav" style="left:771px">Pricing</div>

<section class="abs hero"></section>
<ul class="abs ticks">
  <li><svg viewBox="0 0 14 12"><use href="#tick"/></svg>Business Websites</li>
  <li><svg viewBox="0 0 14 12"><use href="#tick"/></svg>Online Marketing</li>
  <li><svg viewBox="0 0 14 12"><use href="#tick"/></svg>Dashboard Controls</li>
  <li><svg viewBox="0 0 14 12"><use href="#tick"/></svg>Full Setup &amp; Support</li>
</ul>
<p class="abs tagline">Getting a Website has<br>never been so simple</p>
<div class="abs signup">SIGN UP NOW FOR FREE!<b></b></div>
<div class="abs person" role="img" aria-label="Photo of a small business owner looking puzzled"></div>
<div class="bubble" style="left:309px;top:128px">Testimonial</div>
<div class="bubble" style="left:423px;top:112px;font-weight:700">PPC</div>
<div class="bubble" style="left:540px;top:103px">Hosting</div>
<div class="bubble" style="left:666px;top:95px">Blog</div>
<div class="bubble" style="left:693px;top:145px;width:98px">SEO</div>
<div class="bubble" style="left:406px;top:163px;width:112px">Email Marketing</div>
<div class="bubble" style="left:363px;top:200px">Referrals</div>
<div class="bubble" style="left:710px;top:195px">News</div>
<div class="bubble" style="left:418px;top:232px">Website Design</div>
<div class="bubble" style="left:306px;top:250px;width:106px;font-size:10px">Content Management</div>
<div class="bubble" style="left:725px;top:247px">Social Page</div>
<div class="bubble" style="left:402px;top:290px">Images</div>
<div class="bubble" style="left:710px;top:302px">Micro Feeds</div>

<section class="abs band">
  <h1>The Complete Online Marketing Solution for small business website</h1>
  <p>"Get a big online prensence and more sales leads in 30minutes"</p>
</section>
<h2 class="abs how">How does it work?</h2>

<div class="abs tile setup">
  <div class="corner"></div>
  <div class="price">£199<small>Value</small></div>
  <svg class="burst" viewBox="0 0 100 100"><use href="#star" fill="#fff"/></svg>
  <div class="burst"><span style="font-size:16px">FREE</span></div>
  <div class="lead" style="top:96px"><em style="font-size:26px;line-height:30px">SETUP</em></div>
  <div class="foot">WEB OFFER ONLY</div>
</div>
<div class="abs tile pro">
  <div class="corner" style="border-top-color:#22b14c"></div>
  <div class="price" style="color:#222">£22<small style="color:#fff">Per month</small></div>
  <svg class="burst" viewBox="0 0 100 100"><use href="#star" fill="#fff"/></svg>
  <div class="burst"><span>PRO<br>PACKAGE</span></div>
  <div class="lead" style="top:106px">BIG ONLINE<em>PRESENCE</em></div>
  <div class="foot">BUSINESS WEBSITE<br>&amp; EASY DASHBOARD</div>
</div>
<div class="abs tile turbo">
  <div class="corner"></div>
  <div class="price">£29<small>Per month</small></div>
  <svg class="burst" viewBox="0 0 100 100"><use href="#star" fill="#fff"/></svg>
  <div class="burst"><span>TURBO<br>SALES<br>PRO PLUS</span></div>
  <div class="lead" style="top:94px">MORE SALES<em style="font-size:24px;line-height:28px">LEADS</em></div>
  <div class="foot">BUSINESS WEBSITE,EASY<br>DASHBOARD &amp; PPC SALES</div>
</div>
<div class="abs divider"></div>

<div class="abs slider"></div>
<div class="abs arrow prev"></div>
<div class="abs thumb" style="left:91px" role="img" aria-label="Screenshot of a salon client website"></div>
<div class="abs thumb" style="left:268px" role="img" aria-label="Screenshot of a salon client website"></div>
<div class="abs thumb" style="left:445px" role="img" aria-label="Screenshot of a salon client website"></div>
<div class="abs thumb" style="left:623px" role="img" aria-label="Screenshot of a salon client website"></div>
<div class="abs arrow next"></div>

<div class="abs author">Ms.Reed<small>Lorem ipsum</small></div>
<blockquote class="abs quote">Lorem ipsum dolor sit amet, consectetuer adipiscing elit. &nbsp;Lorem ipsum dolor sit amet, consectetuer adipiscing elit. &nbsp;Lorem ipsum dolor sit amet, consectetuer adipiscing elit.</blockquote>

<div class="abs card" style="left:56px"><h3>Case Studies</h3><div class="ico" role="img" aria-label="Report document with chart icon" style="background:linear-gradient(#f4f4f4,#d8d8d8)"></div><p>Lorem ipsum dolor sit amet, consectetuer adipiscing elit.</p></div>
<div class="abs card" style="left:249px"><h3>How to</h3><div class="ico" role="img" aria-label="Target with dart icon" style="background:radial-gradient(#d9232d 30%,#fff 31% 55%,#d9232d 56%);border-radius:50%"></div><p>Lorem ipsum dolor sit amet, consectetuer adipiscing elit.</p></div>
<div class="abs card" style="left:442px"><h3>News &amp; Chatter</h3><div class="ico" role="img" aria-label="Speech bubbles icon" style="background:linear-gradient(135deg,#3fb6f0,#f7b520)"></div><p>Lorem ipsum dolor sit amet, consectetuer adipiscing elit.</p></div>
<div class="abs card" style="left:634px"><h3>Demo</h3><div class="ico" role="img" aria-label="Megaphone icon" style="background:linear-gradient(135deg,#f58a1f,#d7321a)"></div><p>Lorem ipsum dolor sit amet, consectetuer adipiscing elit.</p></div>

<footer class="abs footer"></footer>
<ul class="abs fcol" style="left:74px;line-height:13px"><li>Search Marketing<br>Organic/Natiral (SEO)</li><li style="margin-top:6px">Social Media</li><li style="margin-top:6px">Web Analytics</li></ul>
<ul class="abs fcol" style="left:242px"><li>Contact Us</li><li>Costomer Support</li><li>Request a Call back</li><li>FAQ's</li></ul>
<ul class="abs fcol" style="left:417px"><li>Site Map</li><li>Terms and conditions</li></ul>
<div class="abs fcol news" style="left:605px;top:1081px;width:200px"><h4>Signup for monthly Newsletters</h4><div class="field">Enter your email</div><div class="go">GO</div></div>
<div class="abs copy">Copyright © 2012 zverda.com</div>
</body>
</html>
```